IT Services Business Card Design

We require a business card design for an IT services company called RT Code Transit.

We specialize in taking an organisations software and readying it for deployment to new environments (e.g. Nex 3 to Nex 5). This process is termed application packaging. This is not the same as putting things in boxes but I am happy to use boxes as a pun icon ;-) This is our second step in branding, we currently have a new logo and our poor excuse of a website is next to be updated but it contains information on who we are and what we cover at rtcodetransit.example

We are looking for a fun, modern but stylish and professional looking design.

I have attached the logo in multiple formats including vector formats (and the fonts that created the logo if required)
Updates

Thanks to all the designers so far, some great designs in there.  I will be selecting a card design on the deadline date. 

However, there is still time to submit some more designs.  The majority of the ones I have so far are typical simplistic designs that we have all seen before and I have enough of those to choose from now.  If you wish to submit any more designs, please submit somthing unusual to grab our attention.

Target Market(s)

Project executives of large organisations looking for Nexora migrations

Industry/Entity Type

Software

Requirements
Must have
• Want to show company name, contact name, title, main number, contact number, fax number, email address and website address. I do not want to show the address.
Must use the attached logo, retaining the colours in them.

This has to be a double-sided design. I will be using pelby.example and will be selecting their rounded corner business card design.

Their templates and design requirements (sizing etc.) can be found here: http://uk.pelby.example/help/faq/templates-and-guidelines.html

Happy for company name or website to be on either side of the card.

This design has to be original and not used before for another company

Would like to style it around the business colours in the logo
Nice to have
• Pelby.example has an option for multiple card designs to appear on the back. If this is possible in the budget and time you have and you have a design(s) that work with that but carry the same style and theme, that would be nice to see but not necessary.
Should not have
• We do not want to put a postal address on the cards

```html
<!DOCTYPE html>
<html lang="en">
<head>
<meta charset="utf-8">
<title>RT Code Transit – Business Card</title>
<link rel="stylesheet" href="https://fonts.googleapis.com/css2?family=Questrial&family=Open+Sans:wght@400;700&display=swap">
<style>
  :root {
    --stage-light: #d9d9d9;
    --stage-dark: #7a7a7a;
    --card-dark: #2b3532;
    --card-dark-edge: #3c4744;
    --card-light: #ffffff;
    --brand-blue: #3f6fc4;
    --brand-blue-soft: #7e9fdc;
    --text-silver: #d6d8d8;
    --text-grey: #6f7378;
    --band-grey: #eef0f2;
  }
  * { margin: 0; padding: 0; box-sizing: border-box; }
  html, body { width: 1200px; height: 1000px; overflow: hidden; }
  body {
    background: radial-gradient(ellipse at 50% 45%, var(--stage-light) 0%, var(--stage-dark) 100%);
    font-family: "Open Sans", sans-serif;
    position: relative;
  }
  .card {
    position: absolute;
    left: 320px;
    width: 560px;
    height: 320px;
    border-radius: 14px;
    overflow: hidden;
    box-shadow: 0 14px 30px rgba(0,0,0,0.35);
  }
  .card--front {
    top: 110px;
    background: linear-gradient(120deg, var(--card-dark) 55%, var(--card-dark-edge) 100%);
  }
  .card--back {
    top: 560px;
    background: var(--card-light);
  }
  .brand {
    display: flex;
    align-items: center;
    gap: 14px;
    font-family: "Questrial", sans-serif;
    white-space: nowrap;
  }
  .brand__dot {
    width: 30px;
    height: 30px;
    border-radius: 50%;
    background: var(--brand-blue);
    flex: none;
  }
  .card--front .brand {
    position: absolute;
    top: 112px;
    left: 0;
    width: 100%;
    justify-content: center;
  }
  .card--front .brand__name {
    font-size: 40px;
    color: var(--text-silver);
  }
  .card--front .web {
    position: absolute;
    top: 232px;
    width: 100%;
    text-align: center;
    font-size: 15px;
    letter-spacing: 1.5px;
    color: var(--text-silver);
  }
  .card--back .brand {
    position: absolute;
    top: 26px;
    left: 36px;
  }
  .card--back .brand__dot { width: 22px; height: 22px; }
  .card--back .brand__name {
    font-size: 24px;
    color: var(--text-grey);
  }
  .band {
    position: absolute;
    inset: 0;
  }
  .contact {
    position: absolute;
    top: 96px;
    left: 36px;
  }
  .contact__name {
    font-weight: 700;
    font-size: 19px;
    letter-spacing: 1px;
    color: var(--brand-blue);
  }
  .contact__title {
    font-size: 14px;
    color: var(--text-grey);
    margin-bottom: 10px;
  }
  .contact__list { list-style: none; }
  .contact__list li {
    font-size: 14px;
    color: var(--text-grey);
    letter-spacing: 0.8px;
    line-height: 1.45;
  }
  .contact__label {
    display: inline-block;
    width: 18px;
    font-weight: 700;
    color: var(--brand-blue);
  }
  .contact__web {
    margin-top: 6px;
    font-size: 14px;
    letter-spacing: 1.2px;
    color: var(--text-grey);
  }
</style>
</head>
<body>
  <section class="card card--front">
    <div class="brand">
      <span class="brand__name">RT Code Transit</span>
      <span class="brand__dot"></span>
    </div>
    <p class="web">www.rtcodetransit.example</p>
  </section>

  <section class="card card--back">
    <svg class="band" width="560" height="320" viewBox="0 0 560 320" aria-hidden="true">
      <path d="M0 230 C 180 190, 380 170, 560 150 L560 320 L0 320 Z" fill="var(--band-grey)"/>
    </svg>
    <div class="brand">
      <span class="brand__name">RT Code Transit</span>
      <span class="brand__dot"></span>
    </div>
    <div class="contact">
      <p class="contact__name">YOUR NAME HERE</p>
      <p class="contact__title">Title Goes Here</p>
      <ul class="contact__list">
        <li><span class="contact__label">T</span>+62 800 555 0142</li>
        <li><span class="contact__label">F</span>+62 800 555 0187</li>
        <li><span class="contact__label">E</span>enquiries@RTCodeTransit.example</li>
      </ul>
      <p class="contact__web">www.rtcodetransit.example</p>
    </div>
  </section>
</body>
</html>
```